Visitenkarten/Briefpaier/Kassenkassenbelege für Juwelier
Zielgruppe
Mittelständischer Juwelier mit zwei Filialen. Klassischer Schmuck, Uhren und Modeschmuck
Aufgabenstellung
Es müssen für zwei Geschäfte Visitenkarten, Briefpapier (A4) und Kassenkassenbelege (A6) erstellt werden. Logo und Typo im Anhang. Ein Farbkonzept besteht noch nicht. Die Idee geht in Richtung Bordeaux-Rot.
Generell:
(1) Sieht erstmal nach viel Beschreibung aus, bitte nicht entmutigen lassen, sind zu 90% nur austauschbare Inhalts-/Kontaktdaten.
(2) Für meine Zwecke reicht es vollkommen aus, wenn bei den Vorschlägen zur Arbeitsersparnis erstmal nur mit einer Adresse gearbeitet wird. Wenn ich dann den zutreffenden Designvorschlag gefunden habe, können wir die zweite Adresse in dem ersten Format umsetzen. Ich denke das spart Zeit und Nerven.
(3) Bitte Angaben wie "Tel.:" oder "USt.- ID:" nicht wörtlich nehmen, es soll dabei klar sein worum es geht; wenn "Telefon" ausgeschrieben besser aussieht, bitte in der optisch ansprechenderen Form verwenden.
(4) Bei Fragen, bitte fragen!
(5) Viel Spass bei dem Projekt - Ich freu' mich auf die Vorschläge!
Visitenkarten(1):
Juwelier Brandhoff GmbH
www.juwelier-brandhoff-beispiel.de
Visitenkarten(2):
Visitenkarten(generell):
(1) Die einzelnen Daten können durch Hervorhebungen wie Adresse, Kontakt, Online/Internet unterteilt bzw. hervorgehoben werden.
(2) Die Visitenkarten sollen farbig gedruckt werden; geplant ist weiß als Hintergrund ist aber nicht zwingend bei einer guten anderen Idee
Briefpapier:
(1)Absender im Adressfeld für DIN-lang Briefumschläge mit Fenster:
(2)Informationen im Footer/Seitenbereich:
Juwelier Brandhoff Gmb..

```html
<!DOCTYPE html>
<html lang="de">
<head>
<meta charset="utf-8">
<title>Juwelier Brandhoff – Geschäftsausstattung</title>
<link href="https://fonts.googleapis.com/css2?family=Source+Sans+3:wght@400;600;700&display=swap" rel="stylesheet">
<style>
:root{
  --stage:#4a070b;
  --bordeaux:#7c0f16;
  --bordeaux-dark:#5c0a0f;
  --gold:#e2b522;
  --gold-soft:#f0cf5a;
  --cream:#f5ecd6;
  --paper:#ffffff;
  --ink:#3a3a3a;
  --label-bg:#000000;
  --label-fg:#ffffff;
}
*{box-sizing:border-box;margin:0;padding:0}
html,body{width:1200px;height:1200px;overflow:hidden}
body{background:var(--stage);font-family:"Source Sans 3",Arial,sans-serif;position:relative;color:var(--ink)}

.label{position:absolute;z-index:2}
.label-title{display:inline-block;background:var(--label-bg);color:var(--label-fg);font-weight:700;font-size:26px;padding:4px 12px}
.label-sub{display:block;width:max-content;background:var(--label-bg);color:var(--label-fg);font-size:18px;padding:3px 12px;margin-top:6px}

.brand{display:flex;align-items:center;gap:8px;color:var(--gold);font-weight:600;text-transform:uppercase;letter-spacing:.06em;white-space:nowrap}
.brand-square{background:var(--gold);flex:none}
.gold-text{color:var(--gold)}

/* Kassenbon */
.receipt{position:absolute;left:137px;top:200px;width:333px;height:456px;background:var(--paper);display:flex;flex-direction:column}
.receipt-head{height:106px;background:var(--bordeaux);display:flex;justify-content:space-between;align-items:center;padding:0 14px;border-bottom:4px solid var(--paper);box-shadow:0 3px 0 var(--bordeaux)}
.receipt-head .brand{font-size:15px}
.receipt-head .brand-square{width:14px;height:14px}
.receipt-address{font-size:8.5px;line-height:1.45;text-align:right}
.receipt-body{flex:1;background:linear-gradient(160deg,var(--cream),var(--paper) 70%);margin-top:6px}
.receipt-note{font-size:7.5px;text-align:center;padding:8px 30px 10px;line-height:1.35}
.receipt-foot{font-size:7px;display:flex;justify-content:space-between;padding:6px 12px 10px;border-top:1px solid #ddd;white-space:nowrap}

/* Briefpapier */
.letter{position:absolute;left:560px;top:150px;width:480px;height:679px;background:var(--paper);display:flex;flex-direction:column}
.letter-head{height:112px;background:var(--bordeaux);display:flex;justify-content:space-between;align-items:center;padding:0 18px 0 60px;flex:none}
.letter-head .brand{font-size:19px}
.letter-head .brand-square{width:16px;height:16px}
.letter-address{font-size:7.5px;line-height:1.4;text-align:right;align-self:flex-start;padding-top:10px}
.letter-address-gap{display:block;height:5px}
.letter-rules{height:9px;border-bottom:2px solid var(--bordeaux);margin-top:4px;border-top:2px solid var(--bordeaux);flex:none}
.letter-sender{font-size:5.5px;padding:6px 0 0 30px}
.letter-body{flex:1;background:linear-gradient(165deg,var(--cream),var(--paper) 75%);margin-top:8px}
.letter-foot{display:grid;grid-template-columns:1.3fr 1.3fr 1fr 1fr;gap:10px;font-size:5.6px;line-height:1.5;padding:10px 18px 14px}

/* Visitenkarten */
.card{position:absolute;width:318px;height:200px;background:var(--bordeaux)}
.card-front{left:230px;top:745px;background:repeating-linear-gradient(135deg,var(--bordeaux) 0 10px,var(--bordeaux-dark) 10px 11px);display:flex;align-items:center;justify-content:center}
.card-front .brand{font-size:20px;flex-direction:column;gap:10px}
.card-front .brand-square{width:20px;height:20px}
.card-back{left:140px;top:918px;display:flex}
.card-back-main{width:52%;padding:20px 10px 18px;display:flex;flex-direction:column;justify-content:space-between;align-items:center}
.card-back-main .brand{font-size:11px;letter-spacing:.03em;flex-direction:column;gap:6px}
.card-back-main .brand-square{width:12px;height:12px}
.card-back-address{font-size:8.5px;line-height:1.45;text-align:center}
.card-back-side{width:48%;background:repeating-linear-gradient(135deg,var(--bordeaux-dark) 0 8px,var(--bordeaux) 8px 9px);display:flex;flex-direction:column;padding:14px 6px 18px}
.card-ornament{height:84px;width:84px;margin:0 auto;border-radius:50%;background:radial-gradient(circle,var(--gold-soft),var(--gold) 60%,transparent 62%)}
.card-contact{font-size:7px;line-height:1.5;margin-top:auto;white-space:nowrap}
</style>
</head>
<body>

<div class="label" style="left:65px;top:135px"><span class="label-title">Kassenbon</span><span class="label-sub">A6</span></div>

<section class="receipt">
  <header class="receipt-head">
    <div class="brand"><span class="brand-square"></span>Juwelier Brandhoff</div>
    <div class="receipt-address gold-text">Juwelier Brandhoff GmbH<br>Lindenallee 12<br>45000 Musterstadt<br><br>Tel.: 0123 - 45 67 89<br>Fax: 0123 - 45 67 90</div>
  </header>
  <div class="receipt-body" role="img" aria-label="Zartes Facettenmuster in Creme als Hintergrund"></div>
  <p class="receipt-note">Bei Umtausch oder Reklamation bitte Beleg vorlegen. Barauszahlung ganz oder teilweise ausgeschlossen.</p>
  <footer class="receipt-foot"><span>info@juwelier-brandhoff-beispiel.de</span><span>www.juwelier-brandhoff-beispiel.de</span><span>USt.-ID: DE</span></footer>
</section>

<section class="letter">
  <header class="letter-head">
    <div class="brand"><span class="brand-square"></span>Juwelier Brandhoff</div>
    <div class="letter-address gold-text">Juwelier Brandhoff GmbH<br>Lindenallee 12<br>45000 Musterstadt<span class="letter-address-gap"></span>Tel.: 0123 - 45 67 89<br>Fax: 0123 - 45 67 90<span class="letter-address-gap"></span>info@juwelier-brandhoff-beispiel.de<br>www.juwelier-brandhoff-beispiel.de</div>
  </header>
  <div class="letter-rules"></div>
  <p class="letter-sender">Juwelier Brandhoff GmbH, Lindenallee 12 in 45000 Musterstadt</p>
  <div class="letter-body" role="img" aria-label="Zartes Facettenmuster in Creme als Hintergrund"></div>
  <footer class="letter-foot">
    <div>Bankverbindung:<br>Beispielbank AG Musterstadt<br>IBAN: DE00 0000 0000 0000 0000 00<br>BIC: BSPBDE00</div>
    <div>Amtsgericht Musterstadt HRB 00000<br>Geschäftsführer: Anna Brandhoff<br><br>Steuernummer: 000/0000/0000<br>USt.-ID: DE 000000000</div>
    <div>Filiale:<br>Marktgasse 4<br>45999 Beispielstadt</div>
    <div>Beispielstadt<br>Tel.: 0987 - 65 43 21<br>Fax: 0987 - 65 43 22</div>
  </footer>
</section>

<div class="label" style="left:900px;top:1040px"><span class="label-title">Briefpapier</span><span class="label-sub">A4</span></div>

<div class="label" style="left:95px;top:680px"><span class="label-title">Visitenkarte</span><span class="label-sub">Vorne</span></div>

<section class="card card-front">
  <div class="brand"><span class="brand-square"></span>Juwelier Brandhoff</div>
</section>

<section class="card card-back">
  <div class="card-back-main">
    <div class="brand"><span class="brand-square"></span>Juwelier Brandhoff</div>
    <div class="card-back-address gold-text">Juwelier Brandhoff GmbH<br>Lindenallee 12<br>45000 Musterstadt</div>
  </div>
  <div class="card-back-side">
    <div class="card-ornament" role="img" aria-label="Goldenes Schmuckornament"></div>
    <div class="card-contact gold-text">Tel.: 0123 - 45 67 89<br>Fax: 0123 - 45 67 90<br>info@juwelier-brandhoff-beispiel.de</div>
  </div>
</section>

<div class="label" style="left:470px;top:1060px"><span class="label-title">Visitenkarte</span><span class="label-sub">Hinten</span></div>

</body>
</html>
```